Werbe Flyer an Hausbesitzer
Zielgruppe
Wir sind ein Immobilien Makler in Zürich. Wir werden den Werbe-Flyer zusammen mit einem Begleitschreiben und einem Rückantwort-Briefumschlag an Hausbesitzer per Post senden.
Zielgruppe:
ältere Leute, die Ihr Haus oder Wohnung verkaufen möchten.
Ziel:
Wir möchten den Maklerauftrag bekommen
Aufgabenstellung
Ein Werbe-Flyer erstellen.
Format:
A5
4 Seiten (Also A4 quer einmal gefaltet)
Hochformat
ein Beispiel liegt bei.
Der Text ist bereits definitiv.
Bilder und Layout ist frei wählbar.
Letzte Seite sollte abgetrennt werden können für die Rücksendung
Unsere Webpage als Info evtl. für Layout:
www.velaro-haus.ch

```html
<!DOCTYPE html>
<html lang="de">
<head>
<meta charset="utf-8">
<title>Velaro Immobilien AG – Flyer</title>
<link rel="stylesheet" href="https://fonts.googleapis.com/css2?family=Lato:wght@300;400;700&family=Roboto+Condensed:ital,wght@1,400&display=swap">
<style>
:root{
  --stage:#7a7a7a;
  --paper:#ffffff;
  --band-top:#e4e4e4;
  --band-bottom:#f7f7f7;
  --navy:#1f3e6e;
  --blue:#2d5a93;
  --ink:#333333;
  --rule:#8a8a8a;
  --teal:#2bb3c9;
}
*{margin:0;padding:0;box-sizing:border-box}
html,body{width:915px;height:1200px;overflow:hidden}
body{background:var(--stage);font-family:"Lato",sans-serif;font-weight:300;color:var(--ink);position:relative}
.sheet{position:absolute;left:66px;width:773px;height:546px;background:var(--paper);box-shadow:5px 5px 6px rgba(0,0,0,.45);overflow:hidden}
.sheet--outside{top:35px}
.sheet--inside{top:620px}
.header-band{position:absolute;left:0;top:0;width:100%;height:117px;background:linear-gradient(90deg,var(--band-top),#f2f2f2 60%,#dcdcdc)}
.fold{position:absolute;left:382px;top:0;width:1px;height:117px;background:#cfcfcf}
.brand{position:absolute;top:40px;display:flex;align-items:center;gap:8px;color:var(--navy);font-weight:400;font-size:30px;letter-spacing:1px;line-height:1}
.brand-mark{width:22px;height:22px;background:var(--navy)}
.abs{position:absolute}
.kicker{color:var(--blue);font-size:11px;font-weight:400;letter-spacing:.3px}
.reply-note{font-size:9.5px}
.reply-strong{font-size:9.5px;font-weight:400;color:#111}
.check{position:absolute;left:80px;width:17px;height:17px;border:1px solid #999}
.check-label{position:absolute;left:103px;font-size:10px}
.field{position:absolute;left:80px;width:278px;border-top:1px solid var(--rule);padding-top:2px;font-size:9px}
.reply-address{left:80px;top:510px;font-size:9.5px;line-height:12.5px;letter-spacing:.2px}
.photo{position:absolute}
.claim{left:415px;top:418px;color:#fff;font-size:19px;line-height:24px;letter-spacing:.4px}
.web{left:607px;top:498px;color:#fff;font-size:15px;font-weight:400}
.contact{left:470px;top:33px;font-size:10px;line-height:13.5px;color:#222}
.partner-head{left:79px;top:132px;font-size:12px;line-height:16px;color:#222}
.quote{left:33px;top:186px;font-family:"Roboto Condensed",sans-serif;font-style:italic;color:var(--navy);font-size:15px;line-height:18.5px}
.service{position:absolute;left:416px;width:330px}
.service h3{color:var(--blue);font-weight:400;font-size:10.5px;letter-spacing:.2px;margin-bottom:8px}
.service p{margin-left:55px;font-size:8.8px;line-height:12px;color:#222}
.footer-band{position:absolute;left:0;top:495px;width:100%;height:51px;background:linear-gradient(180deg,#e8e8e8,#d8d8d8)}
.footer-label{left:39px;top:507px;font-size:9px}
.consultant{position:absolute;top:507px;font-size:9px;line-height:12px}
.consultant b{display:block;color:var(--blue);font-weight:400;font-size:9.5px}
</style>
</head>
<body>

<section class="sheet sheet--outside">
  <div class="header-band"></div>
  <div class="fold"></div>

  <div class="brand" style="left:40px"><span class="brand-mark"></span>VELARO</div>
  <div class="brand" style="left:416px"><span class="brand-mark"></span>VELARO</div>

  <!-- reply card -->
  <div class="abs kicker" style="left:39px;top:132px">RÜCKANTWORT</div>
  <div class="abs reply-note" style="left:80px;top:152px">Einfach abtrennen und im beigefügten Rückumschlag an uns senden</div>
  <div class="abs reply-strong" style="left:80px;top:176px">Bitte kreuzen Sie Ihre Wünsche an.</div>
  <div class="abs reply-strong" style="left:80px;top:202px">Ja, wir möchten …</div>

  <span class="check" style="top:227px"></span><span class="check-label" style="top:234px">… unsere Immobilie verkaufen</span>
  <span class="check" style="top:259px"></span><span class="check-label" style="top:266px">… eine Immobilie kaufen</span>
  <span class="check" style="top:291px"></span><span class="check-label" style="top:298px">… ein persönliches Gespräch</span>

  <div class="field" style="top:342px">Name/Vorname</div>
  <div class="field" style="top:373px">Strasse</div>
  <div class="field" style="top:405px">PLZ/Ort</div>
  <div class="field" style="top:436px">Telefon</div>
  <div class="field" style="top:467px">E-Mail</div>

  <div class="abs reply-address">VELARO IMMOBILIEN AG | SEEFELDGASSE 27 | 8008 ZÜRICH<br>Fax 044 600 12 35 | info@velaro-haus.ch | www.velaro-haus.ch</div>

  <svg class="abs" style="left:371px;top:507px" width="14" height="18" viewBox="0 0 14 18" aria-hidden="true">
    <g fill="none" stroke="#444" stroke-width="1">
      <circle cx="3" cy="15" r="2.2"/><circle cx="10" cy="15" r="2.2"/>
      <line x1="4.5" y1="13.4" x2="9" y2="1"/><line x1="8.5" y1="13.4" x2="5" y2="1"/>
    </g>
  </svg>

  <!-- cover -->
  <div class="photo" role="img" aria-label="Alpenpanorama mit schneebedeckten Gipfeln über dem Zürichsee mit Brücke und Altstadt" style="left:385px;top:117px;width:388px;height:429px;background:linear-gradient(180deg,#7f9bc0 0%,#d9dde6 14%,#8a97ad 30%,#4d5b72 44%,#6b6f6c 54%,#3a5c8c 66%,#2d4f80 100%)"></div>
  <div class="photo" role="img" aria-label="Modernes weisses Einfamilienhaus mit Wintergarten" style="left:607px;top:68px;width:146px;height:100px;background:linear-gradient(180deg,#cfe0f0,#eef0ee 45%,#6c8a4a)"></div>
  <div class="photo" role="img" aria-label="Weisses Wohnhaus mit Balkon und blühendem Garten" style="left:607px;top:171px;width:146px;height:110px;background:linear-gradient(180deg,#6aa0d8,#e8e6e0 50%,#5d8a3c)"></div>
  <div class="photo" role="img" aria-label="Neues weisses Einfamilienhaus mit dunklem Dach" style="left:607px;top:284px;width:146px;height:104px;background:linear-gradient(180deg,#3f7ed0,#f2f2f2 50%,#4f7a36)"></div>
  <div class="photo" role="img" aria-label="Moderne gelbe und weisse Mehrfamilienhäuser" style="left:607px;top:391px;width:146px;height:95px;background:linear-gradient(120deg,#5a8fd0 0%,#e6e4dd 45%,#d9b843 75%,#6b8c4a 100%)"></div>

  <div class="abs claim">IMMOBILIEN<br>SIND UNSERE<br>LEIDENSCHAFT</div>
  <div class="abs web">www.velaro-haus.ch</div>
</section>

<section class="sheet sheet--inside">
  <div class="header-band"></div>
  <div class="brand" style="left:40px"><span class="brand-mark"></span>VELARO</div>

  <div class="abs contact">VELARO IMMOBILIEN AG<br>Seefeldgasse 27<br>8008 Zürich<br>Tel. 044 600 12 30<br>Fax 044 600 12 35<br>info@velaro-haus.ch</div>
  <div class="photo" role="img" aria-label="Bürogebäude der Firma mit dunkler Holzfassade" style="left:607px;top:22px;width:146px;height:111px;background:linear-gradient(180deg,#dfe5ec,#8a7868 35%,#5e4c3e 75%,#9a9a96)"></div>

  <div class="abs partner-head">IHRE PARTNER FÜR ALLE FRAGEN<br>RUND UM IHRE IMMOBILIE</div>

  <div class="photo" role="img" aria-label="Zürcher Altstadt mit Kirchtürmen und Alpen im Hintergrund, davor die beiden Berater im Anzug" style="left:0;top:170px;width:463px;height:325px;background:linear-gradient(90deg,rgba(255,255,255,0) 70%,#fff 100%),linear-gradient(180deg,#fff 0%,#d6dde8 35%,#9aa8bb 60%,#6f7f94 100%)"></div>
  <div class="photo" role="img" aria-label="Zwei Berater im dunklen Anzug" style="left:108px;top:172px;width:245px;height:323px;background:linear-gradient(180deg,rgba(40,40,45,0) 0%,rgba(40,40,45,.55) 30%,#2a2a30 60%,#1e1e22 100%)"></div>

  <div class="abs quote">„Wir setzen uns für<br>&nbsp;jede Liegenschaft<br>&nbsp;ein, als wäre es<br>&nbsp;unsere Eigene.“</div>

  <div class="service" style="top:132px">
    <h3>UNSERE DIENSTLEISTUNGEN</h3>
    <p>Der Kauf und Verkauf von Immobilien ist Vertrauenssache. Aus diesem Grund geniesst bei Velaro Immobilien AG die persönliche Beziehung zum Kunden neben allen fachlichen Aspekten in jeder Phase höchste Priorität. So behalten Sie stets den Überblick und bleiben in jeder Phase auf dem Laufenden.</p>
  </div>
  <div class="service" style="top:225px">
    <h3>SCHÄTZUNG</h3>
    <p>Es gibt viele Gründe, sich auch ohne Verkaufsabsichten hin und wieder über den Wert seiner eigenen Immobilie zu informieren. Wir übernehmen für Sie auf Wunsch die genaue und objektive Wertbeurteilung von Einfamilienhaus und Grundstück.</p>
  </div>
  <div class="service" style="top:306px">
    <h3>VERKAUF</h3>
    <p style="margin-top:10px">Ist ein Verkauf geplant, überprüfen wir für Sie im Vorfeld die aktuellen Verkaufsmöglichkeiten. Dazu gehören sowohl die Ermittlung eines realistischen Verkaufspreises als auch die Erstellung detaillierter Verkaufsunterlagen. Auch Objektbesichtigungen führen wir für Sie durch.</p>
  </div>
  <div class="service" style="top:402px">
    <h3>BEURKUNDUNG UND ÜBERTRAGUNG</h3>
    <p>Neben Schätzung Ihrer Liegenschaft und Marketing führen wir für Sie auch die Preisverhandlungen mit potentiellen Interessenten. Zudem erstellen wir mit dem zuständigen Notariat den Entwurf und die Ausarbeitung der Kaufverträge und begleiten Sie bis zur Beurkundung und Eigentumsübertragung auf dem Grundbuchamt.</p>
  </div>

  <div class="footer-band"></div>
  <div class="abs footer-label">The creative consultants</div>
  <div class="consultant" style="left:146px"><b>MARC-ANDRÉ KELLER</b>Tel. direkt 044 600 12 34</div>
  <div class="consultant" style="left:261px"><b>STEFAN B. HUBER</b>Tel. direkt 044 600 12 30</div>
</section>

</body>
</html>
```